Elegant and Professional Business card design needed

The client journey mentor is a company which provides consulting services to businesses to assist them in improving the customer experience for their customers.

I need a business card design which tells people I'm there to help them.

Target Market(s)

Small to medium business owners

Industry/Entity Type

Business

Contact Information for Business Card

Leonard Pashcroft
The Client Journey Mentor
Web: http://www.TheClientJourneyMentor.example
Email: leonard@TheClientJourneyMentor.example
Phone: +61 452 386017

Logo styles of interest
Abstract Logo
Requirements
Must have
• Some sort of image / graphic representing the customer is important and should be at the heart of a business.

```html
<!DOCTYPE html>
<html lang="en">
<head>
<meta charset="UTF-8">
<title>Leonard Pashcroft – The Client Journey Mentor</title>
<link rel="stylesheet" href="https://fonts.googleapis.com/css2?family=Crimson+Pro:wght@400&family=Arimo:wght@400;700&family=PT+Sans:wght@400&display=swap">
<style>
  :root {
    --stage: #26303c;
    --card-light: #f8fbfc;
    --card-edge: #dbe8ef;
    --name-blue: #1b5a83;
    --name-green: #3a9b4a;
    --ink-grey: #585a5c;
    --band-green: #3aa047;
    --band-green-deep: #2f9a42;
    --on-band: #ffffff;
  }
  * { margin: 0; padding: 0; box-sizing: border-box; }
  html, body {
    width: 1200px;
    height: 970px;
    overflow: hidden;
    background: var(--stage);
  }
  .business-card {
    position: absolute;
    left: 75px;
    top: 186px;
    width: 1050px;
    height: 600px;
    overflow: hidden;
    background: radial-gradient(ellipse 70% 80% at 72% 38%, var(--card-light) 0%, #eef4f7 55%, var(--card-edge) 100%);
    box-shadow: 0 10px 30px rgba(0,0,0,0.45);
  }
  .holder-name {
    position: absolute;
    left: 58px;
    top: 62px;
    font-family: "Crimson Pro", "Palatino Linotype", serif;
    font-size: 52px;
    line-height: 1;
    white-space: nowrap;
  }
  .holder-name .given { color: var(--name-blue); }
  .holder-name .family { color: var(--name-green); }
  .holder-email {
    position: absolute;
    left: 105px;
    top: 124px;
    font-family: "Arimo", Arial, sans-serif;
    font-size: 16px;
    color: var(--ink-grey);
  }
  .client-mark {
    position: absolute;
    left: 462px;
    top: 244px;
    width: 50px;
    height: 50px;
  }
  .company-name {
    position: absolute;
    right: 60px;
    top: 236px;
    font-family: "Crimson Pro", "Palatino Linotype", serif;
    font-size: 40px;
    line-height: 66px;
    color: var(--ink-grey);
    text-align: right;
    white-space: nowrap;
  }
  .company-name span { display: block; }
  .company-name .line-one { margin-right: 298px; }
  .contact-band {
    position: absolute;
    left: 0;
    top: 355px;
    width: 1050px;
    height: 140px;
  }
  .band-phone {
    position: absolute;
    left: 63px;
    top: 412px;
    font-family: "Arimo", Arial, sans-serif;
    font-weight: 700;
    font-size: 31px;
    color: var(--on-band);
    text-shadow: 0 1px 2px rgba(0,0,0,0.25);
  }
  .band-web {
    position: absolute;
    right: 40px;
    top: 412px;
    font-family: "PT Sans", "Myriad Pro", sans-serif;
    font-size: 30px;
    color: var(--on-band);
  }
</style>
</head>
<body>
  <div class="business-card">
    <div class="holder-name"><span class="given">Leonard</span> <span class="family">Pashcroft</span></div>
    <div class="holder-email">leonard@TheClientJourneyMentor.example</div>

    <svg class="client-mark" viewBox="0 0 50 50" role="img" aria-label="Circle standing for the client at the heart of the business">
      <circle cx="25" cy="25" r="24" fill="var(--name-blue)"/>
    </svg>

    <div class="company-name">
      <span class="line-one">The Client</span>
      <span class="line-two">Journey Mentor</span>
    </div>

    <svg class="contact-band" viewBox="0 0 1050 140" aria-hidden="true">
      <defs>
        <linearGradient id="band-fill" x1="0" y1="0" x2="0" y2="1">
          <stop offset="0" stop-color="#4daa55"/>
          <stop offset="1" stop-color="#2f9a42"/>
        </linearGradient>
        <filter id="band-shadow-blur" x="-10%" y="-200%" width="120%" height="500%">
          <feGaussianBlur stdDeviation="3"/>
        </filter>
      </defs>
      <ellipse cx="515" cy="123" rx="405" ry="5" fill="rgba(0,0,0,0.55)" filter="url(#band-shadow-blur)"/>
      <path d="M0 29 H835 C848 29 852 22 856 13 Q860 6 864 13 C868 22 872 29 885 29 H1050 V122 H0 Z" fill="url(#band-fill)"/>
    </svg>

    <div class="band-phone">+61 452 386017</div>
    <div class="band-web">www.TheClientJourneyMentor.example</div>
  </div>
</body>
</html>
```